Business incubator; Angel investments; Consulting for startups

We need new office equipment

Target Market(s)

Start up Company

Font styles to use
Sans Serif

Colors

Designer to choose only greyscale colors for use in the design.

Requirements
Must have
• Existing company logo
Nice to have
• Corporate according to the website www.twm-norvane.com
Should not have
• Colors off gray

```html
<!DOCTYPE html>
<html lang="en">
<head>
<meta charset="utf-8">
<title>TWM Norvane Letterhead</title>
<link rel="stylesheet" href="https://fonts.googleapis.com/css2?family=Montserrat:wght@400;500;600;700&family=Poppins:wght@300;400&family=Allura&display=swap">
<style>
  :root {
    --paper: #ffffff;
    --ink: #262626;
    --ink-soft: #4a4a4a;
    --ink-muted: #6b6b6b;
    --body: #6a6a6a;
    --rule: #a6a7a9;
    --mark: #6d6c6b;
    --band-light: #a7a8aa;
    --band-dark: #6f6e6d;
  }
  html, body { margin: 0; padding: 0; overflow: hidden; }
  body { width: 992px; height: 1200px; background: var(--paper); position: relative; font-family: "Montserrat", sans-serif; color: var(--ink); }

  .header-rule { position: absolute; top: 180px; height: 8px; background: var(--rule); border-radius: 2px; }
  .header-rule--left { left: 26px; width: 375px; }
  .header-rule--right { left: 593px; width: 374px; }
  .brand-mark { position: absolute; left: 410px; top: 27px; width: 172px; height: 160px; background: var(--mark); border-radius: 16px; display: flex; flex-direction: column; align-items: center; justify-content: center; color: #fff; font-weight: 600; font-size: 22px; line-height: 1.2; letter-spacing: 1px; text-align: center; }

  .recipient { position: absolute; left: 26px; top: 306px; }
  .recipient__to { font-size: 15px; color: var(--ink); }
  .recipient__name { font-size: 19px; font-weight: 600; letter-spacing: 0.8px; margin-top: 1px; }
  .recipient__role { font-size: 14.5px; color: var(--ink-soft); margin-top: 3px; letter-spacing: 0.3px; }
  .recipient__contact { margin-top: 12px; font-size: 14px; line-height: 21.5px; color: var(--ink-muted); }
  .recipient__address { color: var(--ink); font-weight: 600; }

  .letter-date { position: absolute; right: 25px; top: 372px; font-size: 14px; color: var(--ink-soft); }
  .letter-date strong { color: var(--ink); font-weight: 600; }

  .letter-body { position: absolute; left: 26px; top: 500px; width: 942px; font-family: "Poppins", sans-serif; font-weight: 300; font-size: 15.6px; line-height: 24.5px; color: var(--body); text-align: justify; }
  .letter-body p { margin: 0 0 24px; }

  .sign-off { position: absolute; left: 26px; top: 905px; }
  .sign-off__signature { font-family: "Allura", cursive; font-size: 34px; color: var(--ink); line-height: 1; }
  .sign-off__name { font-size: 17px; font-weight: 700; letter-spacing: 0.8px; margin-top: 8px; }
  .sign-off__title { font-size: 13.5px; font-weight: 600; letter-spacing: 1.5px; color: var(--ink-muted); margin-top: 7px; }

  .footer { position: absolute; left: 0; top: 1147px; width: 992px; height: 53px; }
  .footer__bands { position: absolute; inset: 0; }
  .footer__company { position: absolute; left: 29px; top: 4px; font-size: 22px; font-weight: 700; color: var(--band-light); letter-spacing: 0.3px; }
  .footer__item { position: absolute; color: #fff; font-family: "Poppins", sans-serif; font-size: 11.5px; line-height: 15px; }
  .footer__phone { left: 328px; top: 14px; }
  .footer__web { left: 523px; top: 4px; }
  .footer__address { left: 746px; top: 4px; }
</style>
</head>
<body>
  <header>
    <div class="header-rule header-rule--left"></div>
    <div class="brand-mark"><span>TWM</span><span>NORVANE</span></div>
    <div class="header-rule header-rule--right"></div>
  </header>

  <section class="recipient">
    <div class="recipient__to">To</div>
    <div class="recipient__name">Owen Hartley</div>
    <div class="recipient__role">CEO, LUMACRAFT</div>
    <div class="recipient__contact">
      <div>P: +91 90000 4821, +91 80000 3376</div>
      <div>W: hello@lumacraft.com, www.lumacraft.com</div>
      <div class="recipient__address">A: 47 Lake View Road, Ranpur, India 500283</div>
    </div>
  </section>

  <div class="letter-date"><strong>Date:</strong> 24-03-2018</div>

  <main class="letter-body">
    <p>Lorem ipsum dolor sit amet, consectetur adipiscing elit. Pellentesque dictum, ante non ullamcorp er convallis, nunc quam blandit metus, ac mollis eros felis a orci. Donec congue, mauris ut pulvinar lobortis, dolor massa feugiat nisi, at tincidunt metus leo vel elit. Proin facilisis semper lobortis. Vivamus augue purus, cursus quis urna non, accumsan pellentesque est. Nulla in iaculis magna, quis aliqu et ex. Cras efficitur metus eget purus euismod facilisis. Proin non metus tincidunt, auctor ipsum a, tempor mi.</p>
    <p>Nulla egestas vulputate risus, ut vestibulum diam commodo id. Mauris ornare libero eu erat portt itor ultrices. Proin sed lectus scelerisque ligula bibendum sagittis ac nec leo. Donec ac accumsan diam, et lobortis mauris.</p>
    <p>Nulla congue volutpat nisl ac lobortis. Integer dignissim interdum libero, quis feugiat velit pretium at. Phasellus sit amet libero rutrum, feugiat odio et, tempus purus.</p>
    <p>Nulla congue volutpat nisl ac lobortis. Integer dignissim interdum libero, quis feugiat velit pretium at. Phasellus sit amet libero rutrum, feugiat odio et, tempus purus. Cras ultricies.</p>
  </main>

  <section class="sign-off">
    <div class="sign-off__signature">Digital Signature</div>
    <div class="sign-off__name">LENA MARSH</div>
    <div class="sign-off__title">CHAIRMAN</div>
  </section>

  <footer class="footer">
    <svg class="footer__bands" width="992" height="53" viewBox="0 0 992 53" aria-hidden="true">
      <rect x="0" y="44" width="992" height="9" fill="var(--band-light)"/>
      <polygon points="327,0 493,0 459,44 293,44" fill="var(--band-light)"/>
      <polygon points="499,0 723,0 689,44 465,44" fill="var(--band-dark)"/>
      <polygon points="729,0 992,0 992,44 695,44" fill="var(--band-light)"/>
    </svg>
    <div class="footer__company">TWM NORVANE PLC</div>
    <div class="footer__item footer__phone">+44 (0) 203 555 0182</div>
    <div class="footer__item footer__web">info@twm-norvane.com<br>www.twm-norvane.com</div>
    <div class="footer__item footer__address">4th Floor, 58 Harrow Lane,<br>London W2C 4KT, United Kingdom</div>
  </footer>
</body>
</html>
```